Create a Valdossi-looking dashboard for our Quiet Harbor Speedometer that can look similar to my AI-generated dashboard attached, but with: 1) clear borders on all four sides, 2) is created in a way that we can modify the numbers weekly, say maybe you create the graphic that we can inset the excel spreadsheet numbers into, but ideally mixed with the Valdossi look black leather bubble design shown in the dashboard?; 3) uses the exact numbers shown in the attachment; 4) the speedometer on top should have four equal colors of red on left (-1), then yellow (0), then light green (1), then medium green (2); 5) the gauge on the top left should be the graphic that includes 0-100% bar that is currently 33%, and right below that a -20 to +20 bar with the arrow pointing to 11.9%, with color coding similar to the graphic; 6) replace the Valdossi logo in the middle with a similar shaped shield with blue background with the "T" logo with the eagle inside it, like attached

```html
<!DOCTYPE html>
<html lang="en">
<head>
<meta charset="utf-8">
<title>Quiet Harbor Speedometer</title>
<link rel="stylesheet" href="https://fonts.googleapis.com/css2?family=Barlow+Semi+Condensed:wght@600;700&family=Montserrat:wght@500;600&family=Open+Sans:wght@500;600&display=swap">
<style>
  :root {
    --bg: #000000;
    --chrome: #c9c9c9;
    --chrome-dark: #8a8a8a;
    --gold: #e8b040;
    --white: #ffffff;
    --navy: #0d1f5c;
    --title-gold: #f5b800;
    --header-text: #b9c8ff;
    --row-text: #1a1a2e;
    --bull: #44d15a;
    --bullish: #86e08a;
    --brakes: #ffff00;
    --reverse: #ff0000;
    --reverse-text: #7a0000;
    --neutral: #c0c0c0;
    --ring-blue: #5b73c4;
    --ring-green: #3dbb4c;
    --ring-red: #c4252a;
    --needle: #d9823a;
    --track: #3a3a3a;
  }
  html, body { margin: 0; padding: 0; background: var(--bg); overflow: hidden; }
  .dashboard { position: relative; width: 1200px; height: 840px; overflow: hidden; background: var(--bg); }
  .dashboard-art { position: absolute; inset: 0; width: 1200px; height: 840px; }
  .label-sm { font-family: "Montserrat", sans-serif; font-weight: 500; fill: var(--white); }
  .gauge-num { font-family: "Open Sans", sans-serif; font-weight: 600; fill: var(--white); }
  .brand-name { font-family: "Barlow Semi Condensed", sans-serif; font-weight: 700; fill: var(--white); }

  .gear-table {
    position: absolute; left: 239px; top: 574px; width: 722px;
    border-collapse: collapse; table-layout: fixed;
    font-family: "Barlow Semi Condensed", sans-serif; font-weight: 700;
    border: 1px solid var(--title-gold);
  }
  .gear-table col.gear { width: 215px; }
  .gear-table col.trend { width: 330px; }
  .gear-table col.change { width: 177px; }
  .gear-table th, .gear-table td { padding: 0; height: 16.5px; line-height: 16.5px; font-size: 11.5px; border: 1px solid #555; }
  .gear-table .title {
    background: var(--navy); color: var(--title-gold); font-size: 27px; height: 25px; line-height: 25px;
    letter-spacing: 0.5px; border-bottom: 1px solid var(--title-gold);
  }
  .gear-table .col-head th { background: var(--navy); color: var(--header-text); text-decoration: underline; font-weight: 600; }
  .gear-table td { color: var(--row-text); text-align: center; background: var(--neutral); }
  .gear-table td.gear-name { text-align: left; padding-left: 54px; }
  .gear-table td.gear-name span { display: inline-block; width: 20px; text-align: right; margin-right: 6px; }
  .row-bull td.active, .row-bull td.gear-name { background: var(--bull); }
  .row-bullish td.gear-name { background: var(--bullish); }
  .row-bearish td.gear-name { background: var(--brakes); }
  .row-bear td.gear-name { background: var(--reverse); color: var(--reverse-text); }
</style>
</head>
<body>
<div class="dashboard">
  <svg class="dashboard-art" viewBox="0 0 2083 1458" xmlns="http://www.w3.org/2000/svg">
    <defs>
      <clipPath id="dial-clip"><rect x="600" y="400" width="900" height="490"/></clipPath>
      <radialGradient id="zone-red" gradientUnits="userSpaceOnUse" cx="1047" cy="890" r="350">
        <stop offset="0.3" stop-color="#f23a3a"/>
        <stop offset="0.75" stop-color="#a01818"/>
        <stop offset="1" stop-color="#3a0606"/>
      </radialGradient>
      <radialGradient id="zone-yellow" gradientUnits="userSpaceOnUse" cx="1047" cy="890" r="350">
        <stop offset="0.3" stop-color="#ecd040"/>
        <stop offset="0.75" stop-color="#a88c22"/>
        <stop offset="1" stop-color="#3a300a"/>
      </radialGradient>
      <radialGradient id="zone-light-green" gradientUnits="userSpaceOnUse" cx="1047" cy="890" r="350">
        <stop offset="0.3" stop-color="#a6dc58"/>
        <stop offset="0.75" stop-color="#6aa432"/>
        <stop offset="1" stop-color="#24400e"/>
      </radialGradient>
      <radialGradient id="zone-green" gradientUnits="userSpaceOnUse" cx="1047" cy="890" r="350">
        <stop offset="0.3" stop-color="#5aa02a"/>
        <stop offset="0.75" stop-color="#316a18"/>
        <stop offset="1" stop-color="#0f240a"/>
      </radialGradient>
      <linearGradient id="needle-gold" x1="0" y1="1" x2="1" y2="0">
        <stop offset="0" stop-color="#a8741c"/>
        <stop offset="0.5" stop-color="#f7d27a"/>
        <stop offset="1" stop-color="#c8902c"/>
      </linearGradient>
      <radialGradient id="hub-gold" cx="0.4" cy="0.35" r="0.7">
        <stop offset="0" stop-color="#fbe3a0"/>
        <stop offset="0.6" stop-color="#d49a36"/>
        <stop offset="1" stop-color="#8a5a14"/>
      </radialGradient>
    </defs>

    <!-- Center dial: four equal zones -->
    <g class="main-dial" clip-path="url(#dial-clip)">
      <path d="M1047 890 L697 890 A350 350 0 0 1 799.5 642.5 Z" fill="url(#zone-red)"/>
      <path d="M1047 890 L799.5 642.5 A350 350 0 0 1 1047 540 Z" fill="url(#zone-yellow)"/>
      <path d="M1047 890 L1047 540 A350 350 0 0 1 1294.5 642.5 Z" fill="url(#zone-light-green)"/>
      <path d="M1047 890 L1294.5 642.5 A350 350 0 0 1 1397 890 Z" fill="url(#zone-green)"/>
      <circle cx="1047" cy="890" r="330" fill="none" stroke="var(--white)" stroke-width="16" stroke-dasharray="3 25.8" stroke-dashoffset="1.5"/>
      <circle cx="1047" cy="890" r="312" fill="none" stroke="var(--white)" stroke-width="36" stroke-dasharray="6 239" stroke-dashoffset="3"/>
      <circle cx="1047" cy="890" r="352" fill="none" stroke="var(--white)" stroke-width="4"/>
      <circle cx="1047" cy="890" r="372" fill="none" stroke="var(--gold)" stroke-width="6"/>
      <circle cx="1047" cy="890" r="362" fill="none" stroke="var(--gold)" stroke-width="2"/>
      <circle cx="1047" cy="890" r="405" fill="none" stroke="var(--chrome-dark)" stroke-width="10"/>
      <circle cx="1047" cy="890" r="105" fill="var(--bg)" stroke="var(--chrome)" stroke-width="16"/>
    </g>
    <text class="gauge-num" x="828" y="822" font-size="62" text-anchor="middle">-1</text>
    <text class="gauge-num" x="955" y="700" font-size="62" text-anchor="middle">0</text>
    <text class="gauge-num" x="1139" y="700" font-size="62" text-anchor="middle">1</text>
    <text class="gauge-num" x="1272" y="822" font-size="62" text-anchor="middle">2</text>

    <g class="brand-mark">
      <circle cx="1047" cy="612" r="14" fill="var(--navy)" stroke="var(--white)" stroke-width="2"/>
      <text class="brand-name" x="1047" y="660" font-size="26" text-anchor="middle">Quiet Harbor</text>
    </g>

    <polygon points="1054,864 1040,842 1205,742" fill="url(#needle-gold)"/>
    <circle cx="1047" cy="853" r="34" fill="url(#hub-gold)"/>

    <!-- Left gauge: earnings growth + reporting bar -->
    <g class="growth-gauge">
      <circle cx="388" cy="828" r="175" fill="none" stroke="var(--white)" stroke-width="3"/>
      <g fill="none" stroke-width="11">
        <path d="M318.2 735.4 A116 116 0 0 1 367.9 713.8" stroke="#5aa85a"/>
        <path d="M367.9 713.8 A116 116 0 0 1 446 727.5" stroke="#9fce6a"/>
        <path d="M446 727.5 A116 116 0 0 1 504 828" stroke="#cfe3b8"/>
        <path d="M504 828 A116 116 0 0 1 497 867.7" stroke="#f6f2d8"/>
        <path d="M497 867.7 A116 116 0 0 1 454.5 923" stroke="#f2e23a"/>
        <path d="M454.5 923 A116 116 0 0 1 433 935" stroke="#e8a030"/>
        <path d="M433 935 A116 116 0 0 1 410.1 941.9" stroke="#d8402a"/>
      </g>
      <text class="label-sm" x="318" y="716" font-size="17" text-anchor="middle">20%</text>
      <text class="label-sm" x="474" y="723" font-size="17" text-anchor="middle">10%</text>
      <text class="label-sm" x="516" y="806" font-size="17">0%</text>
      <text class="label-sm" x="503" y="898" font-size="17">-10%</text>
      <text class="label-sm" x="440" y="963" font-size="17" text-anchor="middle">-20%</text>
      <polygon points="377,816 383,818 449,687" fill="var(--needle)"/>
      <text class="gauge-num" x="388" y="860" font-size="46" text-anchor="middle">11.9%</text>

      <g class="reporting-bar">
        <rect x="290" y="882" width="150" height="12" rx="6" fill="var(--track)"/>
        <rect x="290" y="882" width="49.5" height="12" rx="6" fill="var(--ring-blue)"/>
        <text class="label-sm" x="290" y="914" font-size="14">0%</text>
        <text class="label-sm" x="365" y="914" font-size="14" text-anchor="middle">33%</text>
        <text class="label-sm" x="440" y="914" font-size="14" text-anchor="end">100%</text>
      </g>
    </g>

    <!-- Companies reporting ring -->
    <g class="reporting-ring">
      <text class="label-sm" x="1580" y="667" font-size="17" text-anchor="middle">Companies Reporting QTD</text>
      <circle cx="1585" cy="776" r="82" fill="none" stroke="var(--white)" stroke-width="24"/>
      <circle cx="1585" cy="776" r="82" fill="none" stroke="var(--ring-blue)" stroke-width="24" stroke-dasharray="170 345.2" transform="rotate(-149.4 1585 776)"/>
      <text class="gauge-num" x="1587" y="747" font-size="20" text-anchor="middle">33%</text>
      <text class="gauge-num" x="1584" y="780" font-size="24" text-anchor="middle">(165/500)</text>
    </g>

    <!-- Companies beating ring -->
    <g class="beating-ring">
      <text class="label-sm" x="1814" y="773" font-size="17" text-anchor="middle">Companies Beating</text>
      <text class="label-sm" x="1814" y="795" font-size="17" text-anchor="middle">Earnings Estimates</text>
      <circle cx="1802" cy="907" r="82" fill="none" stroke="var(--ring-green)" stroke-width="22"/>
      <circle cx="1802" cy="907" r="82" fill="none" stroke="var(--ring-red)" stroke-width="22" stroke-dasharray="128.8 386.4" transform="rotate(-135 1802 907)"/>
      <circle cx="1802" cy="907" r="70" fill="none" stroke="var(--white)" stroke-width="3"/>
      <circle cx="1802" cy="907" r="94" fill="none" stroke="var(--white)" stroke-width="2"/>
      <text class="gauge-num" x="1802" y="920" font-size="38" font-weight="500" text-anchor="middle">75%</text>
    </g>

    <!-- Dashboard outline -->
    <path class="dash-outline" d="M195 1070 C120 1070 80 1010 95 930 L150 760 C190 660 250 640 330 622 C450 600 600 592 700 590 C760 480 900 445 1040 445 C1190 445 1320 480 1380 592 C1500 594 1650 602 1760 627 C1850 652 1900 702 1940 800 L1990 960 C2005 1030 1960 1075 1890 1072 C1830 1070 1700 1010 1480 910 C1460 900 1450 898 1430 898 L660 898 C640 898 620 902 600 910 L230 1062 C215 1068 205 1070 195 1070 Z" fill="none" stroke="var(--chrome)" stroke-width="12" stroke-linejoin="round"/>
  </svg>

  <table class="gear-table">
    <colgroup><col class="gear"><col class="trend"><col class="change"></colgroup>
    <thead>
      <tr><th class="title" colspan="3">QUIET HARBOR SPEEDOMETER</th></tr>
      <tr class="col-head"><th>GEAR</th><th>CURRENT TREND</th><th>LAST TREND CHANGE</th></tr>
    </thead>
    <tbody>
      <tr class="row-bull"><td class="gear-name"><span>2</span>TURBO BOOST</td><td class="active">BULL</td><td class="active">Friday, August 15, 2025</td></tr>
      <tr class="row-bullish"><td class="gear-name"><span>1</span>ACCELERATOR PEDAL</td><td>BULLISH</td><td></td></tr>
      <tr class="row-bearish"><td class="gear-name"><span>0</span>BRAKES</td><td>BEARISH</td><td></td></tr>
      <tr class="row-bear"><td class="gear-name"><span>-1</span>REVERSE</td><td>BEAR</td><td></td></tr>
    </tbody>
  </table>
</div>
</body>
</html>
```